GlintOn Feather Line Toothbrush Backcard Design

We need a toothbrush backcard (toothbrush packaging) design for our new toothbrush. We are one of the leading toothbrush distributor and producer company. At the moment our toothbrushes are selling at Quinby, Kindred Mart, 4-Bright and many more supermarkets and mom-and-pop shops in Thailand. Our toothbrush is emphasized on the soft and slim tip bristles which will not hurt your enamel. Easy to grip handle that will ease of use. These 2 mains point should be communicated through the design.

Our brand name is GlintOn (see attached logo that you can use) and the toothbrush model is Feather Line. We will have 2 series for this model which are Feather Line Extra Soft and Feather Line Medium soft. They are basically differentiated by its packaging colors.

We are looking for the attractive and outstanding design from what available in the market right now. Please see enclosed die cut shape of the packaging. This backcard will hold 3 pieces of toothbrush with clear blister cover.

P.S We are very confident that our product produced with very good quality that's why we want to attract people to try. So when they walk in the aisle we want our toothbrush packaging to be eye catching and welcome customer to try.

Target Market(s)

B+ household consumers age between 18-65 both men and women who has open minded to the new product and willing to spend money without brand royalty.

Font styles to use
Sans Serif

Colors

Designer to choose colors to be used in the design.

Requirements
Must have
• - Logo, and model name
• - Quality mark as following GMP, FDA, ISO9001:2015, ISO22176
• - Attractive character which attract the target clients to try.
• - 2-sided packaging using attached die cut
Nice to have
Should not have
• What other brands have

```html
<!DOCTYPE html>
<html lang="en">
<head>
<meta charset="utf-8">
<title>GlintOn Feather Line Backcards</title>
<link href="https://fonts.googleapis.com/css2?family=Montserrat:wght@700;800&display=swap" rel="stylesheet">
<style>
  :root {
    --bg: #e4e6ea;
    --navy: #1d2f9e;
    --navy-deep: #14207a;
    --leaf-blue: #5f9de8;
    --mint: #19e8c8;
    --sun: #f6c21e;
    --leaf-green: #2f7a3a;
    --logo-ink: #3a3a3a;
    --accent-yellow: #f8c21a;
    --accent-red: #d41c2c;
    --white: #ffffff;
    --blister: rgba(255,255,255,0.22);
  }
  html, body {
    margin: 0; padding: 0;
    width: 1200px; height: 1200px;
    overflow: hidden;
    background: var(--bg);
    font-family: "Montserrat", sans-serif;
  }
  .stage { position: relative; width: 1200px; height: 1200px; }
  .backcard {
    position: absolute; top: 205px;
    width: 300px; height: 790px;
    border-radius: 16px;
    overflow: hidden;
    box-shadow: 0 24px 40px rgba(0,0,0,0.12);
  }
  .backcard--extra { left: 220px; background: var(--navy); }
  .backcard--medium { left: 680px; background: var(--sun); }
  .pattern { position: absolute; inset: 0; }
  .pattern--palms {
    background: linear-gradient(160deg, var(--leaf-blue) 0%, var(--navy) 40%, var(--navy-deep) 70%, var(--leaf-blue) 100%);
  }
  .band-top {
    position: absolute; left: 0; right: 0; top: 0; height: 170px;
    background: var(--mint);
  }
  .pattern--flowers {
    top: 170px;
    background: linear-gradient(170deg, var(--sun) 0%, #e9b81c 35%, var(--leaf-green) 60%, var(--sun) 100%);
  }
  .blister {
    position: absolute; left: 16px; right: 16px; top: 40px; bottom: 34px;
    border: 1.5px solid rgba(255,255,255,0.55);
    border-radius: 14px;
  }
  .series-label {
    position: absolute; top: 20px; width: 100%;
    text-align: center; font-size: 10px; font-weight: 800;
    color: var(--white); letter-spacing: 0.5px;
  }
  .backcard--medium .series-label { color: #1f5e55; }
  .hang-hole {
    position: absolute; top: 46px; left: 50%; transform: translateX(-50%);
    width: 84px; height: 26px; border-radius: 8px;
    background: var(--bg);
  }
  .brand-oval {
    position: absolute; top: 95px; left: 50%; transform: translateX(-50%);
    width: 210px; height: 62px; border-radius: 50%;
    background: var(--white);
    display: flex; align-items: center; justify-content: center; gap: 6px;
  }
  .brand-plain {
    position: absolute; top: 100px; width: 100%;
    display: flex; align-items: center; justify-content: center; gap: 6px;
    height: 52px;
  }
  .brand-name { font-size: 30px; font-weight: 800; color: var(--logo-ink); letter-spacing: 0.5px; }
  .brand-dot { width: 9px; height: 9px; border-radius: 50%; background: var(--accent-yellow); }
  .brushes {
    position: absolute; left: 48px; right: 36px; top: 175px; bottom: 60px;
    border-radius: 40px 40px 30px 30px;
    background: linear-gradient(180deg, rgba(255,255,255,0.85) 0%, rgba(255,255,255,0.6) 30%, rgba(140,230,210,0.75) 55%, rgba(255,255,255,0.7) 100%);
  }
  .model-name {
    position: absolute; left: 26px; bottom: 50px;
    transform-origin: left bottom; transform: rotate(-90deg) translateY(100%);
    font-size: 24px; font-weight: 800; letter-spacing: 3px;
    white-space: nowrap; display: flex; align-items: center; gap: 8px;
  }
  .backcard--extra .model-name { color: var(--accent-yellow); }
  .model-tab {
    position: absolute; left: 0; bottom: 60px; width: 52px; height: 240px;
    background: var(--white); border-radius: 0 8px 8px 0;
  }
  .backcard--medium .model-name { color: var(--accent-red); font-size: 19px; left: 14px; bottom: 78px; }
  .model-star { width: 14px; height: 14px; }
  .quality-marks {
    position: absolute; bottom: 12px; width: 100%;
    text-align: center; font-size: 9px; font-weight: 700; color: var(--white);
  }
</style>
</head>
<body>
<main class="stage">

  <section class="backcard backcard--extra">
    <div class="pattern pattern--palms" role="img" aria-label="Blue tropical palm leaf pattern"></div>
    <div class="blister"></div>
    <div class="series-label">EXTRA SOFT</div>
    <div class="hang-hole"></div>
    <div class="brand-oval">
      <span class="brand-name">GlintOn</span><span class="brand-dot"></span>
    </div>
    <div class="brushes" role="img" aria-label="Three white and mint toothbrushes under clear blister"></div>
    <div class="model-name">Feather Line
      <svg class="model-star" viewBox="0 0 14 14"><path d="M7 0 L8.6 5.4 L14 7 L8.6 8.6 L7 14 L5.4 8.6 L0 7 L5.4 5.4 Z" fill="#f8c21a"/></svg>
    </div>
    <div class="quality-marks">GMP, FDA, ISO9001:2015, ISO22176</div>
  </section>

  <section class="backcard backcard--medium">
    <div class="band-top"></div>
    <div class="pattern pattern--flowers" role="img" aria-label="Tropical flowers and green leaves on yellow"></div>
    <div class="blister"></div>
    <div class="series-label">EXTRA SOFT</div>
    <div class="hang-hole"></div>
    <div class="brand-plain">
      <span class="brand-name">GlintOn</span><span class="brand-dot"></span>
    </div>
    <div class="brushes" role="img" aria-label="Three white and mint toothbrushes under clear blister"></div>
    <div class="model-tab"></div>
    <div class="model-name">Feather Line
      <svg class="model-star" viewBox="0 0 14 14"><path d="M7 0 L8.6 5.4 L14 7 L8.6 8.6 L7 14 L5.4 8.6 L0 7 L5.4 5.4 Z" fill="#f8c21a"/></svg>
    </div>
    <div class="quality-marks">GMP, FDA, ISO9001:2015, ISO22176</div>
  </section>

</main>
</body>
</html>
```